Website for Corvalind Capital, my new firm that raises money from investors to buy, build, own an...

Corvalind Capital needs a website! We are a new company with very experienced people, who invest in, own and build hotel properties, as well as apartments and other commercial real estate. We seek investors for our projects, and we provide safe, secure returns on their investment in our projects. Our new logo is designed to exhibit strength, class and security, and would like our website to continue on this theme. Our name, Corvalind, is a word-play on a Greek word “aristeia”, which means “excellence” and “a warriors finest moment of glory in war”. If you are in business, you realize that much of it is like war, with strategy and moves and opponents and competitors, and ever-changing economic conditions and threats that make business very much like war. We like to think that we are good at business (war), and so have named our company “Corvalind”, using the founders last name and the word “aristeia” combined. Another definition of "aristeia" is "performing at the peak of one's potential after a long struggle"...again, much like business in real life! The website design should exhibit financial security, smart moves, and positive growth towards a bright future.

Target Market(s)

The target market is smart and wealthy investors, with others such as brokers, cities and government agencies, lenders, sellers, partners, etc also looking at it.

Industry/Entity Type

Investment

Number of Pages Required

5+ page

Font styles to use
Sans Serif

Colors
fec214

Requirements
Must have
• Our website should have a landing page, a "about" or bio page, a projects page and a contact us page. Our new logo uses the colors black and gold, so this should be factored in to our site. The site should be simple, yet impactful and impressive. I have actually two logos, which can be mixed and interchanged in a complimentary way, each with their own unique look.
Nice to have
• I have uploaded a couple screenshots of a website i like, and the simplicity I mention.
Should not have
• The site should not be flashy or complicated or complex or "busy"

```html
<!DOCTYPE html>
<html lang="en">
<head>
<meta charset="utf-8">
<title>Corvalind Capital</title>
<link href="https://fonts.googleapis.com/css2?family=Open+Sans:ital,wght@0,400;0,600;0,700;1,400;1,600&family=Oswald:wght@400;500&family=Lora:wght@400;700&display=swap" rel="stylesheet">
<style>
:root{
  --gold:#fec214;
  --gold-soft:#fde7a0;
  --gold-pale:#fff3c9;
  --navy:#0d3b66;
  --ink:#111;
  --text:#222;
  --muted:#555;
  --dark:#2b2b2b;
  --black:#0b0b0b;
  --grey:#f1f1f1;
  --white:#fff;
}
*{box-sizing:border-box;margin:0;padding:0}
html,body{width:1200px;height:2177px;overflow:hidden;background:var(--white)}
body{position:relative;font-family:"Open Sans",sans-serif;color:var(--text)}
.abs{position:absolute}

/* top bar */
.topbar{left:0;top:0;width:1200px;height:35px;background:var(--black);color:var(--white);font-size:10px}
.social{left:131px;top:7px;display:flex;gap:7px}
.social span{width:21px;height:21px;background:var(--white);border-radius:2px}
.social span:last-child{background:var(--gold)}
.topbar .contact{top:11px;display:flex;align-items:center;gap:6px}

/* header */
.header{left:0;top:35px;width:1200px;height:91px;background:var(--white)}
.brand{left:131px;top:30px;display:flex;align-items:center;gap:8px;font-family:"Open Sans",sans-serif;font-weight:700;font-size:17px;color:var(--ink);letter-spacing:1px}
.brand i{width:18px;height:18px;background:var(--gold);display:block}
.nav{top:33px;font-size:14px;color:var(--ink)}
.nav.active{color:var(--gold);border-bottom:2px solid var(--gold);padding-bottom:6px}
.search{left:1042px;top:32px;width:26px;height:26px;border-radius:50%;background:var(--gold)}

/* hero */
.hero{left:0;top:126px;width:1200px;height:571px;background:linear-gradient(180deg,#4a4fa8 0%,#7a63b8 35%,#b07aa8 55%,#3a2f4a 75%,#1c1a26 100%)}
.hero-title{left:0;top:180px;width:1200px;text-align:center;font-family:"Oswald",sans-serif;font-weight:500;font-size:37px;color:var(--ink)}
.hero-title span{background:var(--gold);padding:0 6px}
.hero-title span.name{color:var(--white);margin-left:2px}
.hero-text{left:400px;top:244px;width:400px;text-align:center;color:var(--white);font-size:13px;line-height:18px}
.btn-hero{left:518px;top:319px;width:164px;height:41px;background:var(--navy);color:var(--white);font-weight:700;font-size:15px;display:flex;align-items:center;justify-content:center}

/* features */
.features{left:0;top:697px;width:1200px;height:214px;background:linear-gradient(135deg,var(--gold-soft) 0%,var(--gold-pale) 50%,var(--gold-soft) 100%)}
.feature{top:30px;width:180px;text-align:center}
.feature .icon{width:70px;height:70px;margin:0 auto;border-radius:50%;background:var(--navy);display:flex;align-items:center;justify-content:center}
.feature h3{font-family:"Oswald",sans-serif;font-weight:400;font-size:15px;color:var(--ink);margin-top:10px}
.feature p{font-size:11px;line-height:15px;color:var(--muted);margin-top:6px}

/* about */
.section-title{font-family:"Lora",serif;font-size:28px;color:var(--ink)}
.rule{height:2px;background:var(--gold);width:47px}
.about-text{left:131px;top:1057px;width:456px;font-size:13px;line-height:18px;color:var(--text)}
.btn-small{background:var(--gold);color:var(--ink);font-size:11px;display:flex;align-items:center;justify-content:center}
.photo{background:linear-gradient(135deg,#5a7fc4,#2c4a86 60%,#dfe7f2)}
.photo.meeting{background:linear-gradient(135deg,#5c5c5c,#8a7a5a 50%,#3a3a3a)}

/* projects */
.projects{left:0;top:1245px;width:1200px;height:537px;background:var(--grey)}
.card{width:231px;height:211px;box-shadow:0 10px 25px rgba(0,0,0,.15)}
.card.hotels{background:linear-gradient(180deg,#5b5e4e,#3a3a2f)}
.card.apartments{background:linear-gradient(180deg,#4a8fd6,#b8503a 70%,#6b6b6b)}
.card.retail{background:linear-gradient(180deg,#6f8a5a,#4d5a46 60%,#8a6e4e)}
.card-caption{left:0;top:112px;width:100%;text-align:center;color:var(--white)}
.card-caption h4{font-family:"Lora",serif;font-weight:400;font-size:21px}
.card-caption p{font-size:11px;line-height:15px;margin-top:8px;padding:0 20px}
.pager{top:1657px;font-size:18px;color:var(--ink)}

/* footer */
.footer{left:0;top:1782px;width:1200px;height:361px;background:var(--dark);color:var(--white)}
.footer h2{font-family:"Lora",serif;font-size:23px;color:var(--gold);font-weight:700}
.footer-text{font-size:13px;line-height:18px}
.contact-row{display:flex;align-items:center;gap:18px;font-size:13px}
.contact-row svg{width:16px;height:16px;fill:var(--white)}
.thumb{width:87px;height:84px;background:linear-gradient(135deg,#9fc0e6,#3d6aa8)}
.listing h5{font-size:15px;font-weight:400}
.listing b{display:block;color:var(--gold);font-size:14px;margin-top:4px}
.message{left:770px;top:129px;width:297px;height:102px;background:#1e1e1e;font-size:10px;font-style:italic;color:#bbb;padding:14px 21px}
.bottombar{left:0;top:2143px;width:1200px;height:34px;background:var(--black);color:var(--white);font-size:10px;font-style:italic;font-weight:600}
</style>
</head>
<body>

<div class="abs topbar">
  <div class="abs social"><span></span><span></span><span></span></div>
  <div class="abs contact" style="left:806px">
    <svg width="14" height="10" viewBox="0 0 14 10"><rect width="14" height="10" fill="#fff"/><path d="M0 0l7 6 7-6" stroke="#000" fill="none"/></svg>
    info@corvalindcapital.com
  </div>
  <div class="abs contact" style="left:980px">
    <svg width="12" height="12" viewBox="0 0 24 24"><path fill="#fff" d="M6.6 10.8a15 15 0 006.6 6.6l2.2-2.2c.3-.3.7-.4 1-.2 1.1.4 2.3.6 3.6.6.6 0 1 .4 1 1V20c0 .6-.4 1-1 1A17 17 0 013 4c0-.6.4-1 1-1h3.5c.6 0 1 .4 1 1 0 1.3.2 2.5.6 3.6.1.3 0 .7-.2 1z"/></svg>
    +99 4120 5538 1
  </div>
</div>

<header class="abs header">
  <div class="abs brand"><i></i>CORVALIND</div>
  <a class="abs nav active" style="left:750px">Home</a>
  <a class="abs nav" style="left:808px">About Us</a>
  <a class="abs nav" style="left:887px">Projects</a>
  <a class="abs nav" style="left:958px">Contact Us</a>
  <div class="abs search">
    <svg width="26" height="26" viewBox="0 0 26 26"><circle cx="12" cy="12" r="4" stroke="#fff" stroke-width="2" fill="none"/><path d="M15 15l4 4" stroke="#fff" stroke-width="2"/></svg>
  </div>
</header>

<section class="abs hero" role="img" aria-label="City skyline of glass towers at dusk under a purple sky">
  <h1 class="abs hero-title"><span>Welcom to</span><span class="name">CORVALIND</span></h1>
  <p class="abs hero-text">Consectetur adipiscing elit, sed do eiusmod tempor incididunt ut labore et dolore magna aliqua. Ut enim ad minim veniam, quis nostrud exercitation</p>
  <a class="abs btn-hero">Work With Us</a>
</section>

<section class="abs features">
  <div class="abs feature" style="left:154px">
    <div class="icon"><svg width="34" height="30" viewBox="0 0 34 30"><rect x="2" y="20" width="5" height="8" fill="#fec214"/><rect x="10" y="15" width="5" height="13" fill="#fec214"/><rect x="18" y="11" width="5" height="17" fill="#fec214"/><rect x="26" y="6" width="5" height="22" fill="#fec214"/><path d="M2 16L12 8l6 4 12-10" stroke="#fec214" stroke-width="2" fill="none"/></svg></div>
    <h3>Lorem Ipsum</h3><p>Consectetur adipiscing elit, sed do eiusmod tempor incidi dunt ut labore</p>
  </div>
  <div class="abs feature" style="left:386px">
    <div class="icon"><svg width="34" height="34" viewBox="0 0 34 34"><circle cx="19" cy="11" r="8" fill="#fec214"/><text x="19" y="15" font-size="11" text-anchor="middle" fill="#0d3b66" font-family="Open Sans,sans-serif" font-weight="700">$</text><path d="M2 24h8l6 2h8l6-4v4l-8 5H2z" fill="#fec214"/></svg></div>
    <h3>Lorem Ipsum</h3><p>Consectetur adipiscing elit, sed do eiusmod tempor incidi dunt ut labore</p>
  </div>
  <div class="abs feature" style="left:624px">
    <div class="icon"><svg width="30" height="32" viewBox="0 0 30 32"><path d="M8 30h16v-4H8zM10 24h12c0-6-3-9-3-12l5 3 3-3-6-8-9 2-4 8 4 1z" fill="#fec214"/></svg></div>
    <h3>Lorem Ipsum</h3><p>Consectetur adipiscing elit, sed do eiusmod tempor incidi dunt ut labore</p>
  </div>
  <div class="abs feature" style="left:856px">
    <div class="icon"><svg width="28" height="32" viewBox="0 0 28 32"><path d="M14 1L2 5v10c0 8 6 13 12 16 6-3 12-8 12-16V5z" fill="#fec214"/><text x="14" y="22" font-size="15" text-anchor="middle" fill="#0d3b66" font-family="Open Sans,sans-serif" font-weight="700">$</text></svg></div>
    <h3>Lorem Ipsum</h3><p>Consectetur adipiscing elit, sed do eiusmod tempor incidi dunt ut labore</p>
  </div>
</section>

<section class="about">
  <h2 class="abs section-title" style="left:282px;top:976px">About Us</h2>
  <div class="abs rule" style="left:282px;top:1034px"></div>
  <p class="abs about-text">Lorem ipsum dolor sit amet, consectetur adipiscing elit, sed do eiusmod te mpor incididunt ut labore et dolore magna aliqua. Ut enim ad minim veniam, quis nostrud exercitation ullamco laboris nisi ut aliquip ex ea com modo consequat. Duis aute irure dolor in reprehenderit in voluptate velit e sse cillum dolore eu fugiat nulla pariatur.</p>
  <a class="abs btn-small" style="left:131px;top:1167px;width:91px;height:24px">Read More</a>
  <div class="abs photo" style="left:636px;top:959px;width:214px;height:166px" role="img" aria-label="Glass office tower seen from below"></div>
  <div class="abs photo meeting" style="left:815px;top:1040px;width:214px;height:166px;border:6px solid #fff;border-width:0 0 0 0" role="img" aria-label="Business team meeting around a table, seen from above"></div>
</section>

<section class="abs projects">
  <svg class="abs" style="left:552px;top:0" width="96" height="39" viewBox="0 0 96 39"><path d="M0 0h96L48 39z" fill="#fff"/></svg>
  <h2 class="abs section-title" style="left:0;top:74px;width:1200px;text-align:center">Projects</h2>
  <div class="abs rule" style="left:553px;top:130px"></div>
  <div class="abs card hotels" style="left:180px;top:168px" role="img" aria-label="Hotel building with palm trees">
    <div class="abs card-caption"><h4>Hotels</h4><p>Lorem ipsum dolor sit amet, consect etur adipiscing elit</p></div>
  </div>
  <div class="abs card apartments" style="left:482px;top:168px" role="img" aria-label="Apartment tower under a blue sky"></div>
  <div class="abs card retail" style="left:782px;top:168px" role="img" aria-label="Shopping mall interior with trees and shoppers"></div>
  <span class="abs pager" style="left:580px;top:412px">&#8249;</span>
  <span class="abs pager" style="left:608px;top:412px">&#8250;</span>
  <a class="abs btn-small" style="left:556px;top:457px;width:90px;height:25px">View All</a>
</section>

<footer class="abs footer">
  <svg class="abs" style="left:552px;top:0" width="96" height="36" viewBox="0 0 96 36"><path d="M0 0h96L48 36z" fill="#f1f1f1"/></svg>
  <h2 class="abs" style="left:131px;top:66px">Contact Us</h2>
  <p class="abs footer-text" style="left:131px;top:124px;width:300px">Lorem ipsum dolor sit amet, consectetur adipisci ng elit, sed do eiusmod tempor incididunt ut labo re et dolore magna aliqua. Ut enim ad minim</p>
  <div class="abs contact-row" style="left:131px;top:202px"><svg viewBox="0 0 24 24"><path d="M12 2a7 7 0 00-7 7c0 5 7 13 7 13s7-8 7-13a7 7 0 00-7-7zm0 9.5a2.5 2.5 0 110-5 2.5 2.5 0 010 5z"/></svg>E210 , Harbor Lane ,  USA</div>
  <div class="abs contact-row" style="left:131px;top:229px"><svg viewBox="0 0 24 24"><path d="M6.6 10.8a15 15 0 006.6 6.6l2.2-2.2c.3-.3.7-.4 1-.2 1.1.4 2.3.6 3.6.6.6 0 1 .4 1 1V20c0 .6-.4 1-1 1A17 17 0 013 4c0-.6.4-1 1-1h3.5c.6 0 1 .4 1 1 0 1.3.2 2.5.6 3.6.1.3 0 .7-.2 1z"/></svg>+99 4120 5538 1</div>
  <div class="abs contact-row" style="left:131px;top:256px"><svg viewBox="0 0 24 24"><path d="M6 2h9v6H6zM3 9h18v11H3zm3 3v2h3v-2zm5 0v2h3v-2zm5 0v2h3v-2z"/></svg>+99 4120 5538 1</div>
  <div class="abs contact-row" style="left:131px;top:283px"><svg viewBox="0 0 24 24"><path d="M2 5h20v14H2zm1 1l9 7 9-7" stroke="#2b2b2b" stroke-width="1.5"/></svg>info@corvalindcapital.com</div>

  <h2 class="abs" style="left:454px;top:66px">Latest Listing</h2>
  <div class="abs thumb" style="left:454px;top:128px" role="img" aria-label="Boutique office building facade"></div>
  <div class="abs listing" style="left:557px;top:149px"><h5>Boutique Space Fernbrook</h5><b>$ 67,000</b></div>
  <div class="abs thumb" style="left:454px;top:239px" role="img" aria-label="Glass office building corner"></div>
  <div class="abs listing" style="left:557px;top:257px"><h5>Office Space Linden Ave</h5><b>$ 16,000</b></div>

  <h2 class="abs" style="left:770px;top:66px">Newsletter</h2>
  <div class="abs message">Your Message</div>
  <a class="abs btn-small" style="left:770px;top:252px;width:92px;height:26px">Send</a>
</footer>

<div class="abs bottombar">
  <span class="abs" style="left:131px;top:10px">Copyright by Corvalind Capital . All Right Reserved © 2018</span>
  <span class="abs" style="left:821px;top:10px">Client Support</span>
  <span class="abs" style="left:916px;top:10px">Privacy Policy</span>
  <span class="abs" style="left:1007px;top:10px">Terms of Use</span>
</div>

</body>
</html>
```